Business Cards for accounting firm

Need a file and design that we can update for our employees when we get a design we like. Logo is attached.
Megan Tolliver CPA
Owner
P.O. Box 418
Harlow Springs 43187
5553628405
megan@brightlanefin.com
www.brightlanefin.com
Accounting

```html
<!DOCTYPE html>
<html lang="en">
<head>
<meta charset="utf-8">
<title>Brightlane Financial – Business Cards</title>
<link href="https://fonts.googleapis.com/css2?family=Montserrat:wght@400;600;700&family=Open+Sans:wght@400&display=swap" rel="stylesheet">
<style>
  :root {
    --sky: #4dcdf6;
    --ink: #3a3f44;
    --text: #1f1f1f;
    --muted: #555a5f;
    --paper: #ffffff;
    --backdrop: #eceef0;
  }
  * { box-sizing: border-box; margin: 0; padding: 0; }
  html, body {
    width: 1200px; height: 900px; overflow: hidden;
    background: var(--backdrop);
  }
  .sheet {
    width: 1200px; height: 900px;
    display: flex; align-items: center; justify-content: center; gap: 40px;
  }
  .card {
    width: 540px; height: 309px;
    background: var(--paper);
    box-shadow: 0 6px 20px rgba(0,0,0,.12);
    position: relative; overflow: hidden;
  }
  .wordmark {
    display: flex; align-items: center; gap: 12px;
    font-family: "Montserrat", sans-serif; font-weight: 700;
    color: var(--ink); line-height: 1.05;
  }
  .wordmark-dot { width: 22px; height: 22px; border-radius: 50%; background: var(--sky); flex: none; }

  /* Back: contact details */
  .card-contact .wordmark { position: absolute; left: 34px; top: 40px; font-size: 27px; width: 260px; }
  .details {
    position: absolute; left: 290px; top: 100px;
    font-family: "Open Sans", sans-serif; font-size: 15px; color: var(--text); line-height: 1.35;
  }
  .details .person-name {
    font-family: "Montserrat", sans-serif; font-weight: 600; font-size: 19px;
    color: var(--sky); margin-bottom: 2px;
  }
  .details .role { margin-bottom: 10px; }
  .links {
    position: absolute; left: 232px; bottom: 24px;
    font-family: "Open Sans", sans-serif; font-size: 14px; color: var(--muted); line-height: 1.4;
  }

  /* Front: brand */
  .card-brand { background: var(--sky); }
  .brand-band {
    position: absolute; left: 0; right: 0; top: 58px; height: 112px;
    background: var(--paper);
    display: flex; align-items: center; justify-content: center;
  }
  .card-brand .wordmark { font-size: 30px; }
  .greeting {
    position: absolute; left: 0; right: 0; top: 188px; text-align: center;
  }
  .greeting .person-name {
    font-family: "Montserrat", sans-serif; font-weight: 700; font-size: 22px; color: var(--ink);
  }
  .greeting .tagline {
    font-family: "Montserrat", sans-serif; font-weight: 400; font-size: 18px; color: var(--ink); margin-top: 2px;
  }
</style>
</head>
<body>
<main class="sheet">
  <section class="card card-contact">
    <div class="wordmark"><span class="wordmark-dot"></span><span>Brightlane Financial</span></div>
    <div class="details">
      <p class="person-name">Megan Tolliver CPA</p>
      <p class="role">Owner</p>
      <p>P.O. Box 418</p>
      <p>Harlow Springs 43187</p>
      <p>5553628405</p>
    </div>
    <div class="links">
      <p>megan@brightlanefin.com</p>
      <p>www.brightlanefin.com</p>
    </div>
  </section>

  <section class="card card-brand">
    <div class="brand-band">
      <div class="wordmark"><span class="wordmark-dot"></span><span>Brightlane Financial</span></div>
    </div>
    <div class="greeting">
      <p class="person-name">Megan Tolliver CPA</p>
      <p class="tagline">Nice to meet you</p>
    </div>
  </section>
</main>
</body>
</html>
```